Stationery for use with Ninefold Ridge reports

I would like to get a stationery design that my firm -- Ninefold Ridge Advisory -- will use as a format for reports that we send our clients. I am specifically looking for a design for use on a piece of paper or letterhead -- not business cards or envelopes.

We are an Africa based US risk intelligence and strategy firm that works with multinational corporations operating in West Africa. Our initial thinking is that we would like a color scheme consistent with our existing logo -- however we are open to other color schemes.

Also, we would like to see at least two separate versions: one with our company name and logo, the other without name and logo.

We also would like font recommendations for the stationary design.

The final design should communicate discreet professionalism and a modern approach, but it should not overshadow the words and information printed on the stationery.

Target Market(s)

Multinational corporations that currently use our products.

Font styles to use
Serif
Sans Serif

Requirements
Must have
• Sense of discreet professionalism that will not overshadow the content we put onto the stationery format.
• We would like to see designs with and without our company name/logo.
• Please suggest fonts that would work with the stationery.
Nice to have
• Ideally colors consistent with out existing logo, though we are open to and even encourage other ideas.
Should not have
• No need for business cards or envelopes.

```html
<!DOCTYPE html>
<html lang="en">
<head>
<meta charset="utf-8">
<title>Ninefold Ridge Advisory — Letterhead</title>
<link rel="stylesheet" href="https://fonts.googleapis.com/css2?family=Open+Sans:wght@400;600&family=Roboto:wght@400&display=swap">
<style>
  :root {
    --backdrop: #d0ecf4;
    --paper: #ffffff;
    --ink-dark: #1f3a48;
    --ink-body: #5a5a5a;
    --ink-contact: #3c4a55;
    --accent-gold: #d9a441;
    --signature-tone: #e6e8ea;
  }
  * { margin: 0; padding: 0; box-sizing: border-box; }
  html, body {
    width: 1200px;
    height: 1200px;
    overflow: hidden;
    background: var(--backdrop);
  }
  .letterhead {
    position: absolute;
    left: 245px;
    top: 97px;
    width: 712px;
    height: 1006px;
    background: var(--paper);
    font-family: "Open Sans", Arial, sans-serif;
    color: var(--ink-body);
  }
  .brand {
    position: absolute;
    left: 38px;
    top: 110px;
    display: flex;
    align-items: center;
    gap: 8px;
  }
  .brand-dot {
    width: 12px;
    height: 12px;
    border-radius: 50%;
    background: var(--accent-gold);
  }
  .brand-name {
    font-family: "Open Sans", Arial, sans-serif;
    font-weight: 600;
    font-size: 19px;
    color: var(--ink-dark);
    letter-spacing: 0.2px;
    background: var(--paper);
    padding-right: 8px;
  }
  .header-rule {
    position: absolute;
    left: 38px;
    right: 39px;
    top: 129px;
    height: 2px;
    background: var(--ink-dark);
  }
  .brand { z-index: 1; }
  .contact {
    position: absolute;
    left: 520px;
    top: 41px;
    font-family: "Roboto", Arial, sans-serif;
    font-size: 12px;
    color: var(--ink-contact);
    line-height: 14px;
  }
  .contact-address { margin-bottom: 8px; }
  .contact-line {
    display: flex;
    align-items: center;
    gap: 6px;
    line-height: 15px;
  }
  .contact-icon { width: 10px; height: 10px; flex: none; }
  .web-highlight { color: var(--accent-gold); }
  .letter-date {
    position: absolute;
    left: 71px;
    top: 300px;
    font-size: 12.5px;
  }
  .letter-body {
    position: absolute;
    left: 71px;
    top: 357px;
    width: 580px;
    font-size: 12.5px;
    line-height: 26px;
  }
  .letter-body p { margin-bottom: 3px; white-space: nowrap; }
  .signoff {
    position: absolute;
    left: 499px;
    top: 697px;
    font-size: 12px;
    line-height: 14px;
    color: var(--ink-contact);
  }
  .signature-area {
    width: 146px;
    height: 46px;
    margin-left: -6px;
    margin-bottom: 6px;
    background: var(--signature-tone);
    border-radius: 4px;
  }
</style>
</head>
<body>
  <main class="letterhead">
    <header>
      <div class="brand">
        <span class="brand-dot"></span>
        <span class="brand-name">Ninefold Ridge Advisory</span>
      </div>
      <div class="header-rule"></div>
      <address class="contact" style="font-style: normal;">
        <div class="contact-address">Your address, city<br>state, ZIP 0000</div>
        <div class="contact-line">
          <svg class="contact-icon" viewBox="0 0 10 10"><path d="M2 1 L4 1 L4.6 3 L3.5 4 Q4.5 5.8 6 6.5 L7 5.4 L9 6 L9 8 Q8 9 6.5 8.6 Q2.5 7.3 1.2 3 Q1 1.8 2 1 Z" fill="var(--accent-gold)"/></svg>
          <span>123-456-2100</span>
        </div>
        <div class="contact-line">
          <svg class="contact-icon" viewBox="0 0 10 10"><rect x="1" y="2.5" width="8" height="5.5" fill="var(--accent-gold)"/><path d="M1 2.5 L5 5.6 L9 2.5" stroke="#fff" stroke-width="0.8" fill="none"/></svg>
          <span>youremail@inboxmail.net</span>
        </div>
        <div class="contact-line">
          <svg class="contact-icon" viewBox="0 0 10 10"><circle cx="5" cy="5" r="4" fill="var(--accent-gold)"/><path d="M1 5 H9 M5 1 Q2.6 5 5 9 M5 1 Q7.4 5 5 9" stroke="#fff" stroke-width="0.7" fill="none"/></svg>
          <span>www.<span class="web-highlight">yourwebsite</span>.com</span>
        </div>
      </address>
    </header>

    <p class="letter-date">Date, 10 September, 2020</p>

    <section class="letter-body">
      <p>This is a sample letter that has been placed to demonstrate typing remat (Your Company). letterhead<br>design. When positioned properly, it will serve to work in harmony with all other elements letterhead.<br>This letterhead design is meant to project an image</p>
      <p>This letterhead design is meant project an image of professionalism reliability. By using simple aligen<br>we have created a very spacious feeling. The simplicity suggest &nbsp;rengththe spaciousnes contributes h<br>aesthetics the layout. These basic qualities along with the (Your Company)</p>
      <p>look and helps reinforce the (Your Company) brand. letterhead design is meant to project an image p<br>design. When positioned properly, it will serve to work in harmony all the other elements letterhead.<br>sionalism and reliability.</p>
      <p>This letterhead design is based on the (Form of your logo) form (Your Company) logo. Each stationery<br>we have created a very spacious feeling. The simplicity suggests strength the spaciousnes contribute<br>part of the (Form of your logo).</p>
    </section>

    <div class="signoff">
      <div class="signature-area" role="img" aria-label="Handwritten signature of Daniel Arvo"></div>
      <div class="signer-name">Daniel Arvo</div>
      <div class="signer-title">Manager</div>
    </div>
  </main>
</body>
</html>
```